BRISK Body Transformations

12 Week Fresh Start Programme

website preview (it's not live yet) :

http://exampletrainer.sitebuildhub.example/preview/7xqwbe.5lp8rt32mmqz7.a1942f8c60e527ab39147996cd8a457f

colour palette:

RGB codes:

Yellow : R 242,G 206,B 130.
Pink : R 248, G 149,B 133
Dark Pink : R 190,G 108,B 106
Blue : R 38.G 69,B 97#4
Grey : R 78,G 110,B 130

Target Market(s)

Female’s wanting to lose weight, sculpt muscle who are lacking in confidence and feel overwhelmed and don’t know where to start in improving their fitness and lifestyle

Font styles to use
Sans Serif

Colors
fee3d4
ffffff

Requirements
Must have
• My specific colour palette - see above

```html
<!DOCTYPE html>
<html lang="en">
<head>
<meta charset="utf-8">
<title>BRISK Body Transformations – 12 Week Fresh Start Programme</title>
<link rel="stylesheet" href="https://fonts.googleapis.com/css2?family=Inter:wght@300;400;700;800&display=swap">
<style>
  :root {
    --stage: #cbcbcb;
    --paper: #f1f2f4;
    --peach: #fee3d4;
    --salmon: #f4998a;
    --rule: #f08c7c;
    --offer-red: #e31e1a;
    --ink: #111111;
    --band-dark: #150b0a;
    --brand-tone: #f2ce82;
    --white: #ffffff;
  }
  html, body {
    margin: 0;
    padding: 0;
    width: 1200px;
    height: 1170px;
    overflow: hidden;
    background: var(--stage);
  }
  .flyer {
    position: absolute;
    left: 186px;
    top: 0;
    width: 776px;
    height: 1095px;
    transform: scale(1.068);
    transform-origin: top left;
    background: var(--paper);
    overflow: hidden;
    font-family: "Inter", Arial, sans-serif;
    color: var(--ink);
  }
  .flyer-shapes {
    position: absolute;
    inset: 0;
  }
  .hero-photo {
    position: absolute;
    left: 0;
    top: 20px;
    width: 510px;
    height: 812px;
    background: linear-gradient(160deg, #f7f7f8 0%, #efe4dc 45%, #e8cdb9 70%, #f4f1ef 100%);
  }
  .headline {
    position: absolute;
    left: 346px;
    top: 52px;
    margin: 0;
    font-weight: 300;
  }
  .headline-duration {
    display: block;
    font-size: 84px;
    line-height: 92px;
    letter-spacing: -3px;
    color: var(--salmon);
  }
  .headline-main,
  .headline-sub {
    display: block;
    font-size: 41px;
    line-height: 54px;
    letter-spacing: -1px;
    color: var(--ink);
  }
  .headline-main strong { font-weight: 700; }
  .headline-rule {
    position: absolute;
    left: 346px;
    top: 255px;
    width: 380px;
    height: 2px;
    background: var(--rule);
  }
  .intro-copy {
    position: absolute;
    left: 346px;
    top: 276px;
    width: 390px;
    margin: 0;
    font-size: 19.5px;
    line-height: 25px;
    font-weight: 400;
  }
  .offer-badge {
    position: absolute;
    left: 518px;
    top: 435px;
    width: 192px;
    height: 192px;
    color: var(--white);
    text-align: center;
    font-weight: 800;
  }
  .offer-label {
    position: absolute;
    top: 34px;
    width: 100%;
    font-size: 13px;
    font-weight: 700;
  }
  .offer-amount {
    position: absolute;
    top: 58px;
    width: 100%;
    font-size: 56px;
    line-height: 62px;
    letter-spacing: -1px;
  }
  .offer-off {
    position: absolute;
    top: 120px;
    width: 100%;
    font-size: 38px;
    line-height: 40px;
  }
  .fine-print {
    position: absolute;
    right: 50px;
    top: 804px;
    width: 330px;
    margin: 0;
    font-size: 9.6px;
    line-height: 13px;
    text-align: right;
  }
  .brand-band {
    position: absolute;
    left: 0;
    top: 857px;
    width: 776px;
    height: 148px;
    background: var(--band-dark);
    display: flex;
    align-items: center;
    justify-content: center;
  }
  .brand-name {
    font-size: 62px;
    font-weight: 700;
    letter-spacing: 14px;
    color: var(--brand-tone);
    padding-left: 14px;
  }
  .call-band {
    position: absolute;
    left: 0;
    top: 1005px;
    width: 776px;
    height: 90px;
    background: var(--peach);
    text-align: center;
  }
  .call-line {
    margin: 0;
    font-size: 55px;
    line-height: 90px;
    font-weight: 800;
    letter-spacing: -0.5px;
    color: var(--offer-red);
  }
</style>
</head>
<body>
  <main class="flyer">
    <svg class="flyer-shapes" width="776" height="1095" viewBox="0 0 776 1095">
      <polygon points="200,0 776,0 776,52" fill="var(--peach)"/>
      <polygon points="0,806 776,858 0,858" fill="var(--peach)"/>
    </svg>

    <div class="hero-photo" role="img" aria-label="Photo of a woman in white sportswear measuring her waist with a tape measure"></div>

    <h1 class="headline">
      <span class="headline-duration">12Week</span>
      <span class="headline-main"><strong>Fresh</strong> Start</span>
      <span class="headline-sub">Programme</span>
    </h1>
    <div class="headline-rule"></div>

    <p class="intro-copy">Lorem ipsum dolor sit amet, consectetuer adipiscing elit, sed diam nonummy nibh euismod tincidunt ut laoreet dolore magna aliquam erat volutpat. Ut wisi enim ad minim veniam, quis nostrud exerci tation ullamcorper sus</p>

    <div class="offer-badge">
      <svg width="222" height="222" viewBox="0 0 222 222" style="position:absolute;left:0;top:0">
        <circle cx="114" cy="110" r="96" fill="var(--peach)"/>
        <circle cx="96" cy="96" r="96" fill="var(--offer-red)"/>
      </svg>
      <div class="offer-label">SPECIAL OFFER</div>
      <div class="offer-amount">25%</div>
      <div class="offer-off">OFF*</div>
    </div>

    <p class="fine-print">Lorem ipsum dolor sit amet, consectetuer adipiscing elit, sed diam nonummy nibh euismod tincidunt ut laoreet dolore magna aliquam era</p>

    <section class="brand-band">
      <span class="brand-name">BRISK</span>
    </section>

    <section class="call-band">
      <p class="call-line">CALL 012-555-0148</p>
    </section>
  </main>
</body>
</html>
```